Quillstar Lottery Landing Page -

We are looking for a unique Landing Page design that makes users want to subscribe!
Banner artwork, quillstar promo video (already created), subscription info, product highlights. Why users would want to subscribe.
The initial work was done in PHP. I will provide the website in it's current state in a zip file. The website can be run locally with XAMPP.
Target Market(s)
Anyone who plays the lottery and wants to win more!
Industry/Entity Type
Lottery, USA and Canada (More Countries will be added soon)
Coding
Coded - Design and coding required
Other font styles liked:
- Unzip the the work we have currently done and this should give you a good idea of what direction we are going. We love this theme but now we just need to
Requirements
Must have
- After you unzip the quillstar.zip and open the site using XAMPP

```html
<!DOCTYPE html>
<html lang="en">
<head>
<meta charset="utf-8">
<title>Quillstar Lottery – Play Smarter, Win More!</title>
<link href="https://fonts.googleapis.com/css2?family=Fira+Sans+Condensed:wght@400;600;700;800&family=Fira+Sans+Extra+Condensed:wght@700;800&display=swap" rel="stylesheet">
<style>
  :root{
    --purple-deep:#3a0f8c;
    --purple:#6a0fa0;
    --magenta:#c0156f;
    --pink:#e02a7a;
    --navy:#0f0830;
    --navy-2:#1a0c48;
    --gold:#f6a83c;
    --gold-light:#f2e2a6;
    --gold-dark:#b48e3a;
    --red:#e8262b;
    --red-dark:#a5121a;
    --white:#ffffff;
    --ink:#1c1230;
  }
  *{box-sizing:border-box;margin:0;padding:0}
  html,body{width:1200px;height:2862px;overflow:hidden}
  body{font-family:"Fira Sans Condensed",sans-serif;background:var(--navy);color:var(--white)}
  .page{position:relative;width:1200px;height:2862px;overflow:hidden}
  .backdrop{position:absolute;inset:0;width:1200px;height:2862px}
  .abs{position:absolute}

  .brand{display:flex;align-items:center;gap:12px;font-weight:700;color:var(--white)}
  .brand-dot{border-radius:50%;background:var(--red)}
  .brand--header{left:173px;top:50px;font-size:34px}
  .brand--header .brand-dot{width:34px;height:34px}
  .brand--footer{left:175px;top:2715px;font-size:48px}
  .brand--footer .brand-dot{width:46px;height:46px}

  .hero-title{left:170px;top:198px;font-family:"Fira Sans Extra Condensed",sans-serif;font-weight:800;font-size:68px;line-height:76px;color:var(--gold);text-shadow:0 4px 6px rgba(60,0,40,.45)}
  .btn{display:flex;align-items:center;justify-content:center;border-radius:28px;font-weight:700;color:var(--white);box-shadow:0 6px 10px rgba(40,0,30,.45)}
  .btn--subscribe{left:170px;top:387px;width:155px;height:52px;font-size:24px;background:linear-gradient(#f0343a,var(--red-dark))}
  .hero-art{left:615px;top:70px;width:545px;height:490px;border-radius:44% 40% 46% 42%;background:radial-gradient(circle at 45% 60%,#e8312f 0,#d9432a 25%,#e7a233 50%,rgba(90,40,160,.0) 72%)}

  .section-title{left:0;width:1200px;text-align:center;font-weight:700;font-size:40px;color:var(--white);text-shadow:0 3px 5px rgba(0,0,0,.4)}
  .section-title--video{top:698px}
  .section-title--features{top:1298px}

  .video{left:174px;top:778px;width:852px;height:462px;border:3px solid var(--white);border-radius:30px;overflow:hidden;background:radial-gradient(circle at 50% 50%,#c42a2a 0,#8e1616 55%,#5a0b12 100%)}
  .video-art{position:absolute;left:130px;top:20px;width:560px;height:420px;border-radius:50%;background:radial-gradient(circle,#7a3aa8 0,rgba(122,58,168,.55) 55%,rgba(122,58,168,0) 72%)}
  .play{position:absolute;left:375px;top:200px;width:82px;height:82px}

  .wheel{left:173px;top:1445px;width:440px;height:440px;border-radius:50%;background:radial-gradient(circle,#1c1320 0,#221626 55%,#3a1520 62%,#b31b25 66%,#171015 74%,#c9a257 76%,#8a6a2a 80%,rgba(0,0,0,0) 81%)}
  .wheel-text{left:243px;top:1550px;width:300px;text-align:center}
  .wheel-text h3{font-size:27px;line-height:36px;font-weight:600;margin-bottom:14px}
  .wheel-text p{font-size:14px;line-height:25.5px;color:#e8e2ee}

  .feature{display:flex;align-items:center;width:389px;height:72px;border-radius:36px;padding-left:8px;background:linear-gradient(var(--gold-light),#e3cd86);box-shadow:0 5px 0 var(--gold-dark),0 8px 12px rgba(0,0,0,.4);color:var(--ink);font-weight:600;font-size:22px;line-height:22px}
  .feature-icon{flex:none;width:56px;height:56px;border-radius:50%;background:radial-gradient(circle,#c6a55a,#9c7d34);display:flex;align-items:center;justify-content:center;margin-right:14px}
  .feature-icon svg{width:30px;height:30px}
  .feature--active{background:linear-gradient(#f2333a,#c8141c);box-shadow:0 5px 0 #7e0a10,0 8px 12px rgba(0,0,0,.4);color:var(--white)}
  .feature--active .feature-icon{background:radial-gradient(circle,#c81a22,#8e0c12)}
  .feature--active::before{content:"";position:absolute;left:-18px;top:28px;border:9px solid transparent;border-right:10px solid var(--red)}
  .f1{left:586px;top:1403px}.f2{left:623px;top:1493px}.f3{left:647px;top:1583px}
  .f4{left:647px;top:1673px}.f5{left:623px;top:1766px}.f6{left:586px;top:1856px}

  .bingo-art{left:170px;top:2110px;width:410px;height:390px;border-radius:46% 46% 40% 40%;background:radial-gradient(circle at 45% 60%,#d4262d 0,#8e3fa8 40%,#5b5b7a 58%,rgba(90,30,120,0) 74%)}
  .promo-text{left:598px;top:2168px;width:420px;font-weight:700;font-size:31px;line-height:37.5px;color:var(--gold)}
  .btn--promo{left:600px;top:2302px;width:286px;height:52px;font-size:22px;background:linear-gradient(#f58a2a,#e3431d)}

  .social{left:828px;top:2727px;display:flex;gap:13px}
  .social span{width:40px;height:40px;border-radius:50%;border:2px solid var(--white)}
</style>
</head>
<body>
<main class="page">
  <svg class="backdrop" viewBox="0 0 1200 2862" aria-hidden="true">
    <defs>
      <linearGradient id="heroGrad" x1="0" y1="0" x2="0.3" y2="1">
        <stop offset="0" stop-color="#4a0fa0"/>
        <stop offset="0.45" stop-color="#8a127f"/>
        <stop offset="1" stop-color="#e0286f"/>
      </linearGradient>
      <linearGradient id="sweepGrad" x1="0" y1="0" x2="1" y2="1">
        <stop offset="0" stop-color="#7a12a0"/>
        <stop offset="1" stop-color="#3c0f9a"/>
      </linearGradient>
      <linearGradient id="navyGrad" x1="0" y1="0" x2="0" y2="1">
        <stop offset="0" stop-color="#2a0f5e"/>
        <stop offset="0.25" stop-color="#150a3a"/>
        <stop offset="1" stop-color="#0f0830"/>
      </linearGradient>
      <linearGradient id="promoGrad" x1="0" y1="0" x2="0" y2="1">
        <stop offset="0" stop-color="#3e0f9a"/>
        <stop offset="0.55" stop-color="#8d148a"/>
        <stop offset="1" stop-color="#4a0f9e"/>
      </linearGradient>
    </defs>
    <rect width="1200" height="1140" fill="url(#heroGrad)"/>
    <path d="M380 0 H1200 V470 C1120 620 880 680 720 640 C560 600 520 420 600 300 C680 180 520 60 380 0 Z" fill="url(#sweepGrad)"/>
    <path d="M0 1120 C300 1090 700 1090 1200 1110 V2862 H0 Z" fill="url(#navyGrad)"/>
    <path d="M0 1990 C300 2060 700 2070 1200 1990 V2620 C900 2570 500 2570 0 2610 Z" fill="url(#promoGrad)"/>
    <path d="M0 2610 C500 2570 900 2570 1200 2620 V2862 H0 Z" fill="#12082f"/>
  </svg>

  <div class="brand brand--header abs"><span class="brand-dot"></span>Quillstar Lottery</div>

  <h1 class="hero-title abs">Play Smarter,<br>Win More!</h1>
  <a class="btn btn--subscribe abs">Subscribe</a>
  <div class="hero-art abs" role="img" aria-label="Lottery tickets with coloured lottery balls and a dart"></div>

  <h2 class="section-title section-title--video abs">Our Quillstar Video</h2>
  <div class="video abs">
    <div class="video-art" role="img" aria-label="Video still of lottery tickets, balls and gold coins"></div>
    <svg class="play" viewBox="0 0 82 82" aria-label="Play video">
      <circle cx="41" cy="41" r="38" fill="rgba(255,255,255,.25)" stroke="#fff" stroke-width="4"/>
      <path d="M32 24 L60 41 L32 58 Z" fill="#fff"/>
    </svg>
  </div>

  <h2 class="section-title section-title--features abs">Our Features</h2>
  <div class="wheel abs" role="img" aria-label="Roulette wheel with a dart in the top"></div>
  <div class="wheel-text abs">
    <h3>Quickly Generate<br>Tickets</h3>
    <p>Nemo enim ipsam voluptatem quia voluptas sit aspernatur aut odit aut fugit, sed quia con sequuntur magni dolores eos qui ratione volup tatem sequi nesciunt. Neque porro quisquam est, qui dolorem ipsum quia dolor sit amet, consectetur,</p>
  </div>

  <div class="feature f1 abs"><span class="feature-icon"><svg viewBox="0 0 30 30" fill="none" stroke="#fff" stroke-width="2"><rect x="7" y="5" width="16" height="21" rx="2"/><path d="M11 11h8M11 15h8M11 19h5"/></svg></span>Easily Update the Latest Result</div>
  <div class="feature f2 abs"><span class="feature-icon"><svg viewBox="0 0 30 30" fill="none" stroke="#fff" stroke-width="2"><path d="M12 15V7a2 2 0 0 1 4 0v8l5 1a3 3 0 0 1 2 3l-1 6H13l-4-6a2 2 0 0 1 3-2z"/></svg></span>Quick Selection of Numbers</div>
  <div class="feature feature--active f3 abs"><span class="feature-icon"><svg viewBox="0 0 30 30" fill="none" stroke="#fff" stroke-width="2"><rect x="5" y="10" width="20" height="11" rx="2" transform="rotate(-30 15 15)"/></svg></span>Quickly Generate Tickets</div>
  <div class="feature f4 abs"><span class="feature-icon"><svg viewBox="0 0 30 30" fill="none" stroke="#fff" stroke-width="2"><path d="M5 7h20l-8 9v8l-4-2v-6z"/></svg></span>Absolutely Exclusive Filtering<br>Methods</div>
  <div class="feature f5 abs"><span class="feature-icon"><svg viewBox="0 0 30 30" fill="none" stroke="#fff" stroke-width="2"><circle cx="13" cy="13" r="8"/><path d="M19 19l6 6M9 15l3-3 2 2 3-4"/></svg></span>Past Result Analysis &amp; Search</div>
  <div class="feature f6 abs"><span class="feature-icon"><svg viewBox="0 0 30 30" fill="none" stroke="#fff" stroke-width="2"><circle cx="15" cy="15" r="10"/><text x="15" y="19" fill="#fff" stroke="none" font-size="11" text-anchor="middle" font-family="sans-serif">06</text></svg></span>Lottery Prediction Tool</div>

  <div class="bingo-art abs" role="img" aria-label="Bingo cards with a crowned ball, bingo balls and a dart"></div>
  <p class="promo-text abs">Subscribe monthly for about the same price as a few lottery tickets!</p>
  <a class="btn btn--promo abs">See More Winning Tickets!</a>

  <div class="brand brand--footer abs"><span class="brand-dot"></span>Quillstar Lottery</div>
  <nav class="social abs" aria-label="Social links"><span></span><span></span><span></span><span></span></nav>
</main>
</body>
</html>
```